Website Design - for Energy Efficiency company - large corporate feel

Hi there,
Thanks for checking out this project!
We're a UK based energy efficiency business. We arrange for energy efficient systems to be fitted in people's houses (i.e. efficient boilers, solar panels etc.) However, we do not install them ourselves as we have accredited installers who install on our behalf. Therefore the website should appeal to these businesses and have a very professional corporate feel. The final design should communicate that we are a financially safe large corporation.
Our existing website should not be used for inspiration as the style and content are very outdated (it was from a time when were installers - which we no longer are).
The new website design should use the greens from our logo, however I don't want the site saturated in this colour.
I'm really open to your chosen layout and therefore I'm not a huge fan of including links to websites I like - as I don't want to limit your own creativity. However, I would like it to look corporate (but not too boring and unimaginative).
So here's a few links to websites that I feel give a feel of financially safe / large corporate etc. Although you certainly don't have to design with this style / layout in mind:
http://www.brelvanhub.org.uk/advice
http://www.tolvenrise.co.uk/
http://www.qpwd.org.uk/
http://www.wendrowkeyplot.co.uk/
http://www.ruvasto.co.uk/ (very bad design but looks corporate)
http://www.pellarwatt.org.uk/
http://www.vq.co.uk/ (looks corporate but too busy and boring)
http://www.quellisto.co.uk/business/index.htm
http://www.dormavel.com/
https://www.ostrevan.com/en/index.html
The site is for 4 different audiences:
Consumers | Businesses | Public Sector | Installers
Therefore, it's important that there is some form of way of splitting the site up into these sections (almost like 4 websites in 1). Each section will then have the navigation menu with 7 links.
I've attached our logo (company-logo.jpg) and another logo design we have to display inline with regulations (blue-pact-logo.jpg).
Happy designing, and thank you!

```html
<!DOCTYPE html>
<html lang="en">
<head>
<meta charset="utf-8">
<title>Verdmoor Energy — Home</title>
<link href="https://fonts.googleapis.com/css2?family=Arimo:wght@400;700&family=Roboto:wght@300;400&display=swap" rel="stylesheet">
<style>
  :root {
    --brand-green: #4f8a2b;
    --logo-green: #5fa62d;
    --header-bg: #eef0f2;
    --nav-text: #1c1c1c;
    --white: #ffffff;
    --bar-bg: rgba(240, 240, 238, 0.92);
    --bar-text: #222222;
    --footer-bg: #4b3c31;
    --rule: rgba(255, 255, 255, 0.75);
    --placeholder-top: #7b8577;
    --placeholder-bottom: #5c6858;
    --photo-tone: #7d8a74;
    --body-font: "Arimo", Arial, sans-serif;
    --light-font: "Roboto", Arial, sans-serif;
  }
  * { box-sizing: border-box; margin: 0; padding: 0; }
  html, body { width: 955px; height: 1200px; overflow: hidden; }
  body { position: relative; font-family: var(--body-font); background: var(--white); }

  .site-header {
    position: absolute; left: 0; top: 0; width: 955px; height: 82px;
    background: var(--header-bg); z-index: 2;
  }
  .brand {
    position: absolute; left: 84px; top: 28px;
    display: flex; align-items: center; gap: 8px;
  }
  .brand-mark { width: 34px; height: 34px; border-radius: 50%; background: var(--logo-green); }
  .brand-name {
    font-family: var(--body-font); font-weight: 700; font-size: 26px;
    color: var(--logo-green); letter-spacing: -0.5px;
  }
  .main-nav {
    position: absolute; left: 336px; top: 0; height: 90px;
    display: flex; list-style: none;
  }
  .main-nav li a {
    display: block; height: 90px; line-height: 104px; padding: 0 13px;
    font-size: 12.5px; color: var(--nav-text); text-decoration: none;
  }
  .main-nav li.is-current a {
    background: var(--brand-green); color: var(--white); padding: 0 26px;
  }

  .hero {
    position: absolute; left: 0; top: 82px; width: 955px; height: 463px;
  }
  .hero-scene {
    position: absolute; inset: 0;
    background: linear-gradient(180deg, var(--placeholder-top) 0%, var(--placeholder-bottom) 100%);
  }
  .search-field {
    position: absolute; left: 672px; top: 24px; width: 198px; height: 34px;
    background: var(--white); border: 1px solid #d5d5d5;
    font-size: 13px; color: var(--logo-green); padding: 9px 12px;
  }
  .hero-bar {
    position: absolute; height: 57px; background: var(--bar-bg);
    font-size: 16.5px; color: var(--bar-text);
    display: flex; align-items: center; justify-content: center;
  }
  .hero-bar.primary { left: 145px; top: 239px; width: 666px; }
  .hero-bar.secondary { left: 214px; top: 312px; width: 528px; }

  .intro {
    position: absolute; left: 0; top: 545px; width: 955px; height: 558px;
    background: var(--brand-green); color: var(--white); text-align: center;
  }
  .intro-title {
    font-family: var(--light-font); font-weight: 300; font-size: 27px;
    margin-top: 28px;
  }
  .intro-lead {
    font-size: 18px; line-height: 23px; margin: 17px auto 0; width: 760px;
  }
  .section-rule {
    position: absolute; left: 84px; top: 163px; width: 786px;
    display: flex; align-items: center; gap: 26px;
  }
  .section-rule::before, .section-rule::after {
    content: ""; flex: 1; height: 1px; background: var(--rule);
  }
  .section-rule h2 {
    font-family: var(--light-font); font-weight: 300; font-size: 19px;
  }

  .audience {
    position: absolute; top: 225px; width: 200px; text-align: center;
  }
  .audience-photo {
    width: 130px; height: 130px; border-radius: 50%; margin: 0 auto;
    background: var(--photo-tone);
  }
  .audience h3 {
    font-weight: 400; font-size: 15px; letter-spacing: 0.3px; margin-top: 26px;
  }
  .audience p {
    font-size: 10.5px; line-height: 15.5px; margin-top: 7px;
  }
  .read-more {
    display: inline-block; margin-top: 18px; width: 94px; height: 24px;
    border: 1px solid var(--white); color: var(--white);
    font-family: var(--light-font); font-size: 10.5px; line-height: 22px;
    text-decoration: none;
  }
  .audience.consumers { left: 69px; }
  .audience.businesses { left: 276px; }
  .audience.public { left: 481px; }
  .audience.installers { left: 674px; }

  .site-footer {
    position: absolute; left: 0; top: 1103px; width: 955px; height: 97px;
    background: var(--footer-bg);
  }
  .footer-nav {
    position: absolute; left: 88px; top: 43px; display: flex; gap: 17px; list-style: none;
  }
  .footer-nav a { color: var(--white); font-size: 11px; text-decoration: none; }
  .social {
    position: absolute; left: 703px; top: 36px; display: flex; gap: 6px;
  }
  .social span { width: 21px; height: 21px; display: block; }
  .social .social-one { background: #2fa9df; }
  .social .social-two { background: #e58a1f; }
  .social .social-three { background: #3b5a9a; }
  .scheme-badge { position: absolute; left: 788px; top: 11px; }
</style>
</head>
<body>
  <header class="site-header">
    <div class="brand">
      <span class="brand-mark"></span>
      <span class="brand-name">VERDMOOR</span>
    </div>
    <ul class="main-nav">
      <li class="is-current"><a href="#">home</a></li>
      <li><a href="#">about us</a></li>
      <li><a href="#">blue pact</a></li>
      <li><a href="#">ECO</a></li>
      <li><a href="#">landlords</a></li>
      <li><a href="#">renewables</a></li>
      <li><a href="#">contact us</a></li>
    </ul>
  </header>

  <section class="hero">
    <div class="hero-scene" role="img" aria-label="Hero photograph: city skyline behind a green meadow"></div>
    <div class="search-field">search</div>
    <div class="hero-bar primary">Duis autem vel eum iriure dolor in hendrerit in vulputate velit esse molestie consequat</div>
    <div class="hero-bar secondary">Duis autem vel eum iriure dolor in hendrerit in vulpu</div>
  </section>

  <main class="intro">
    <h1 class="intro-title">Welcome to Verdmoor Energy</h1>
    <p class="intro-lead">Duis autem vel eum iriure dolor in hendrerit in vulputate velit esse molestie consequat, vel illum dolore eu feugiat nulla facilisis at vero eros et accumsan et iusto odio dignissim</p>

    <div class="section-rule"><h2>Our Categories</h2></div>

    <article class="audience consumers">
      <div class="audience-photo" role="img" aria-label="Photograph of a group of consumers"></div>
      <h3>CONSUMERS</h3>
      <p>Lorem ipsum dolor sit amet,<br>consectetuer adipiscing elit, sed<br>diam nonummy nibh euismod<br>tinci volutpat adipisci</p>
      <a class="read-more" href="#">Read more</a>
    </article>
    <article class="audience businesses">
      <div class="audience-photo" role="img" aria-label="Photograph of business people shaking hands"></div>
      <h3>BUSINESSES</h3>
      <p>Lorem ipsum dolor sit amet,<br>consectetuer adipiscing elit, sed<br>diam nonummy nibh euismod<br>tinci volutpat adipisci</p>
      <a class="read-more" href="#">Read more</a>
    </article>
    <article class="audience public">
      <div class="audience-photo" role="img" aria-label="Photograph of public sector workers"></div>
      <h3>PUBLIC SECTORS</h3>
      <p>Lorem ipsum dolor sit amet,<br>consectetuer adipiscing elit, sed<br>diam nonummy nibh euismod<br>tinci volutpat adipisci</p>
      <a class="read-more" href="#">Read more</a>
    </article>
    <article class="audience installers">
      <div class="audience-photo" role="img" aria-label="Photograph of installers fitting solar panels on a roof"></div>
      <h3>INSTALLERS</h3>
      <p>Lorem ipsum dolor sit amet,<br>consectetuer adipiscing elit, sed<br>diam nonummy nibh euismod<br>tinci volutpat adipisci</p>
      <a class="read-more" href="#">Read more</a>
    </article>
  </main>

  <footer class="site-footer">
    <ul class="footer-nav">
      <li><a href="#">about verdmoor</a></li>
      <li><a href="#">consumers</a></li>
      <li><a href="#">businesses</a></li>
      <li><a href="#">public sectors</a></li>
      <li><a href="#">installers</a></li>
      <li><a href="#">contact us</a></li>
    </ul>
    <div class="social">
      <span class="social-one" aria-label="Social link"></span>
      <span class="social-two" aria-label="News feed link"></span>
      <span class="social-three" aria-label="Social link"></span>
    </div>
    <svg class="scheme-badge" width="58" height="74" viewBox="0 0 58 74" role="img" aria-label="Approved scheme badge">
      <rect x="1" y="1" width="56" height="72" fill="#e9efe4"/>
    </svg>
  </footer>
</body>
</html>
```